Bref créative
Business Cards for a Start-Up
Wholesaler of Construction Products
Professional
Marva Quintero
President
472 West Palmera Ln., Ste C204
Hagatna, GU 96842
marva@pacificbedrockco.com
www.pacificbedrockco.com
Reefstone Supply, Inc. is a start-up company that will be wholesaling construction products (e.g., concrete, asphalt, etc.) to prime construction contractors. The business cards should be straight-forward and easy to read. We are colored backgrounds. If you have any questions, please post in the project discussion area.

```html
<!DOCTYPE html>
<html lang="en">
<head>
<meta charset="utf-8">
<title>Reefstone Supply Stationery</title>
<link rel="stylesheet" href="https://fonts.googleapis.com/css2?family=Arimo:wght@400;700&display=swap">
<style>
  :root {
    --paper: #ffffff;
    --edge: #b9b9b9;
    --brand: #6a6b6d;
    --ink: #4a4a4c;
    --ink-soft: #8a8a8c;
  }
  html, body {
    margin: 0;
    padding: 0;
    width: 1200px;
    height: 1101px;
    overflow: hidden;
    background: var(--paper);
    font-family: "Arimo", Arial, sans-serif;
    color: var(--ink);
  }
  .canvas { position: relative; width: 1200px; height: 1101px; }
  .sheet {
    position: absolute;
    background: var(--paper);
    border: 1px solid var(--edge);
    box-sizing: border-box;
  }
  .brand { position: absolute; display: flex; align-items: center; gap: 12px; }
  .brand-square { background: var(--brand); flex: none; }
  .brand-name {
    font-family: "Arimo", Arial, sans-serif;
    font-weight: 700;
    color: var(--brand);
    line-height: 1;
    white-space: nowrap;
  }

  /* Letterhead */
  .letterhead { left: 24px; top: 24px; width: 666px; height: 1032px; }
  .letterhead .brand { left: 26px; top: 26px; }
  .letterhead .brand-square { width: 40px; height: 40px; }
  .letterhead .brand-name { font-size: 30px; }
  .letterhead-footer {
    position: absolute; left: 36px; bottom: 22px;
    font-size: 10px; line-height: 1.6; color: var(--ink-soft);
  }
  .letterhead-footer strong { color: var(--ink); }

  /* Business card */
  .business-card { left: 849px; top: 126px; width: 336px; height: 174px; }
  .business-card .brand { left: 14px; top: 74px; gap: 6px; }
  .business-card .brand-square { width: 16px; height: 16px; }
  .business-card .brand-name { font-size: 12px; }
  .card-holder { position: absolute; left: 186px; top: 22px; }
  .card-name { font-size: 12px; font-weight: 700; color: var(--ink); }
  .card-title { font-size: 8px; color: var(--ink-soft); margin-top: 2px; }
  .card-details {
    position: absolute; left: 186px; top: 66px;
    font-size: 6.5px; line-height: 1.55; color: var(--ink-soft);
  }

  /* Envelope */
  .envelope { left: 369px; top: 570px; width: 816px; height: 405px; }
  .envelope-flap { position: absolute; left: 0; top: 0; }
  .flap-seal {
    position: absolute; left: 396px; top: 118px;
    width: 24px; height: 24px; background: var(--brand);
  }
  .envelope .brand { left: 26px; top: 196px; }
  .envelope .brand-square { width: 40px; height: 40px; }
  .envelope .brand-name { font-size: 30px; }
  .envelope-return {
    position: absolute; left: 36px; bottom: 28px;
    font-size: 10px; color: var(--ink-soft);
  }
</style>
</head>
<body>
<div class="canvas">

  <section class="sheet letterhead">
    <div class="brand">
      <span class="brand-square"></span>
      <span class="brand-name">Reefstone Supply, Inc.</span>
    </div>
    <div class="letterhead-footer">
      472 West Palmera Ln., Ste C204 Hagatna, GU 96842<br>
      P: (671) 555-0142 F: (671) 555-0187 info@pacificbedrockco.com <strong>www.pacificbedrockco.com</strong>
    </div>
  </section>

  <section class="sheet business-card">
    <div class="brand">
      <span class="brand-square"></span>
      <span class="brand-name">Reefstone Supply, Inc.</span>
    </div>
    <div class="card-holder">
      <div class="card-name">Marva Quintero</div>
      <div class="card-title">President</div>
    </div>
    <div class="card-details">
      472 West Palmera Ln., Ste C204<br>
      Hagatna, GU 96842<br>
      P: (671) 555-0142<br>
      F: (671) 555-0187<br>
      marva@pacificbedrockco.com<br>
      www.pacificbedrockco.com
    </div>
  </section>

  <section class="sheet envelope">
    <svg class="envelope-flap" width="816" height="405" viewBox="0 0 816 405" aria-hidden="true">
      <polyline points="0,0 408,150 816,0" fill="none" stroke="#b9b9b9" stroke-width="1"/>
    </svg>
    <span class="flap-seal"></span>
    <div class="brand">
      <span class="brand-square"></span>
      <span class="brand-name">Reefstone Supply, Inc.</span>
    </div>
    <div class="envelope-return">472 West Palmera Ln., Ste C204 Hagatna, GU 96842</div>
  </section>

</div>
</body>
</html>
```